Plumber needs a business card

I need a new business card for my plumbing business. I dont have a logo at the moment but I want business cards that are simple but very professional. I want to look like
Name: Milo Brenton
Address: (just make one up)
Phone: 0497 318 264
Email: milo@fernpost.net
Colors to use:
Blacks, blues, silvers

```html
<!DOCTYPE html>
<html lang="en">
<head>
<meta charset="utf-8">
<title>Milo Brenton Plumbing – Business Card</title>
<link rel="stylesheet" href="https://fonts.googleapis.com/css2?family=Montserrat:wght@400;500;700&display=swap">
<style>
  :root {
    --paper: #ffffff;
    --navy: #0d3a5a;
    --ink-blue: #17476f;
    --black: #111418;
    --silver: #a7adb4;
  }
  html, body {
    margin: 0;
    padding: 0;
    width: 1200px;
    height: 703px;
    overflow: hidden;
    background: var(--paper);
  }
  .card {
    position: relative;
    width: 1200px;
    height: 703px;
    background: var(--paper);
    font-family: "Montserrat", Arial, sans-serif;
  }
  .brand {
    position: absolute;
    top: 75px;
    left: 0;
    width: 100%;
    display: flex;
    flex-direction: column;
    align-items: center;
    color: var(--navy);
  }
  .brand-square {
    display: block;
    width: 160px;
    height: 160px;
    background: var(--navy);
  }
  .brand-name {
    margin: 38px 0 0;
    font-size: 72px;
    font-weight: 700;
    line-height: 1;
    letter-spacing: -0.01em;
    text-transform: uppercase;
  }
  .brand-trade {
    margin: 25px 0 0;
    padding-left: 0.95em;
    font-size: 40px;
    font-weight: 400;
    line-height: 1;
    letter-spacing: 0.95em;
    text-transform: uppercase;
  }
  .address {
    position: absolute;
    top: 560px;
    left: 0;
    width: 100%;
    margin: 0;
    text-align: center;
    color: var(--silver);
    font-size: 22px;
    font-weight: 500;
    letter-spacing: 0.06em;
    white-space: nowrap;
  }
  .divider {
    position: absolute;
    top: 612px;
    left: 300px;
    width: 600px;
    height: 1px;
    background: var(--silver);
    border: 0;
    margin: 0;
  }
  .contact {
    position: absolute;
    left: 0;
    top: 640px;
    width: 100%;
    margin: 0;
    text-align: center;
    color: var(--ink-blue);
    font-size: 32px;
    font-weight: 400;
    line-height: 1.1;
    white-space: nowrap;
  }
  .contact-label {
    color: var(--black);
  }
  .contact-item + .contact-item {
    margin-left: 0.6em;
  }
</style>
</head>
<body>
  <main class="card">
    <header class="brand">
      <span class="brand-square" aria-hidden="true"></span>
      <h1 class="brand-name">Milo Brenton</h1>
      <p class="brand-trade">Plumbing</p>
    </header>
    <p class="address">14 Tallowood Lane, Brackenvale NSW 2483</p>
    <hr class="divider">
    <p class="contact">
      <span class="contact-item"><span class="contact-label">Phone:</span> 0497 318 264</span>
      <span class="contact-item"><span class="contact-label">Email:</span> milo@fernpost.net</span>
    </p>
  </main>
</body>
</html>
```